Vormalink home page design

I need a Home page, heading styles and a button designed for an online learning site.
The site content currently focuses on Brenvasta applications but later it could cover anything.
I am attaching a PDF outlining what I want plus some image files. I don't know what I need to tell you - so please ask me questions if you want.
Target Market(s)
Business users, people working from home who are trying to learn how to do something on the computer.
Number of Pages Required
1 page
Requirements
Must have
- The home page will:
- incorporate my logo
- include at least one scrolling panel of questions/statements. Attached PDF has more information.
- User login area
- maybe in the future it will contain a content search tool

```html
<!DOCTYPE html>
<html lang="en">
<head>
<meta charset="utf-8">
<title>Vormalink – Your online learning center</title>
<link rel="stylesheet" href="https://fonts.googleapis.com/css2?family=Arimo:wght@400;700&family=Nunito:wght@700;800&display=swap">
<style>
:root{
  --blue:#0b5fa8;
  --blue-dark:#044b8c;
  --blue-light:#2a8ee0;
  --navy:#0d3f78;
  --orange:#f7911b;
  --orange-light:#ffb347;
  --text:#222;
  --muted:#555;
  --line:#c8c8c8;
  --pager:#c9c9c9;
}
*{box-sizing:border-box;margin:0;padding:0}
html,body{width:1200px;height:813px;overflow:hidden}
body{position:relative;font-family:Arimo,Arial,sans-serif;color:var(--text);
  background:radial-gradient(ellipse 700px 260px at 620px 60px,#eaf1f8 0%,#fff 70%),#fff}
.site-header{position:absolute;left:0;top:0;width:1200px;height:133px;
  background:linear-gradient(180deg,#e6edf4 0%,#f5f8fb 70%,#fff 100%)}
.brand{position:absolute;left:74px;top:72px;display:flex;align-items:center;gap:10px;
  font-family:Nunito,Arial,sans-serif;font-weight:800;font-size:40px;color:var(--blue);letter-spacing:1px}
.brand-mark{width:26px;height:26px;border-radius:50%;background:var(--orange)}
.tagline{position:absolute;right:73px;top:76px;font-size:32px;color:var(--blue-light);font-family:Arimo,Arial,sans-serif}
.tagline b{color:var(--orange);font-weight:700}
.header-rule{position:absolute;left:700px;right:73px;top:120px;height:1px;background:#cfd6de}
.main-nav{position:absolute;left:0;top:133px;width:1200px;height:44px;
  background:linear-gradient(180deg,#2a8ee0 0%,#0b5fa8 12%,#0a5aa0 60%,#064a8a 100%);
  border-bottom:2px solid #8cc4f0}
.main-nav a{position:absolute;top:0;height:42px;line-height:42px;color:#fff;text-decoration:none;font-size:17px;transform:translateX(-50%)}
.main-nav a.active{left:571px;width:248px;text-align:center;background:#043f78;color:#dde9f5;transform:translateX(-50%)}
.card{position:absolute;top:210px;width:328px;height:487px;border:1px solid var(--line);background:#fff}
.card-head{height:46px;margin:-1px -1px 0;display:flex;align-items:center;padding-left:16px;gap:10px;
  font-family:Nunito,Arial,sans-serif;font-weight:800;font-size:20px;color:#4a2a06}
.card-head::before{content:"";border-left:7px solid currentColor;border-top:5px solid transparent;border-bottom:5px solid transparent}
.card--problem{left:74px}
.card--problem .card-head{background:linear-gradient(180deg,#ffb347,#f7911b)}
.card--expert{left:437px}
.card--expert .card-head{background:linear-gradient(180deg,#3f8fd6,#0b5fa8);color:#0d2a48}
.card-media{margin:12px 12px 0;height:194px;border:1px solid #b9c7d6}
.pager{display:flex;gap:4px;margin:10px 12px 0}
.pager span{width:21px;height:21px;background:var(--pager);color:#555;font-size:16px;text-align:center;line-height:21px}
.pager span.current{background:#e2e2e2;color:var(--blue-light)}
.card-title{margin:26px 12px 0;font-size:20px;line-height:21px;font-weight:700;color:var(--navy)}
.card-text{margin:12px 12px 0;font-size:15px;line-height:22px;color:#333}
.more{display:block;margin:12px 12px 0;font-size:13px;font-weight:700;color:var(--orange);text-decoration:none}
.search{position:absolute;left:800px;top:213px;width:268px;height:37px;border:1px solid var(--line);
  padding-left:10px;font-size:17px;line-height:35px;color:#777}
.search-btn{position:absolute;left:1078px;top:213px;width:49px;height:37px;background:linear-gradient(180deg,#ffb347,#f7911b);
  border:1px solid #e48a14;color:#7a4a10;font-size:18px;text-align:center;line-height:35px}
.advanced{position:absolute;left:801px;top:260px;font-size:12px;font-weight:700;color:var(--orange)}
.login{position:absolute;left:800px;top:293px;width:327px;height:173px;border:1px solid var(--line);padding:0 10px}
.login h2{font-family:Nunito,Arial,sans-serif;font-weight:800;font-size:22px;color:#3a72ad;padding:10px 2px 6px;border-bottom:1px solid #ccc}
.field{display:flex;align-items:center;margin-top:16px;height:30px}
.field label{width:80px;font-size:14px;font-weight:700;color:var(--navy);padding-left:1px}
.field span{width:230px;height:30px;border:1px solid var(--line)}
.field + .field{margin-top:12px}
.forgot{display:block;text-align:center;margin:12px 0 0 80px;font-size:12px;font-weight:700;color:var(--orange)}
.info{position:absolute;left:800px;top:485px;width:327px;height:212px;border:1px solid var(--line);padding:0 10px}
.info section{padding:8px 0 0}
.info section + section{border-top:1px solid #ccc;margin-top:8px}
.info h3{font-size:18px;font-weight:400;color:var(--blue)}
.info p{font-size:12.5px;line-height:20px;color:#333;margin-top:6px}
.info .more{margin:6px 0 0}
.footer-band{position:absolute;left:0;top:741px;width:1200px;height:30px;
  background:linear-gradient(180deg,#c9c9c9,#e6e6e6 30%,#f4f4f4);border-bottom:1px solid #ccc}
.copyright{position:absolute;top:781px;width:1200px;text-align:center;font-size:11.5px;color:#555}
.copyright a{color:var(--blue);text-decoration:none}
</style>
</head>
<body>
<header class="site-header">
  <div class="brand"><span class="brand-mark"></span>Vormalink</div>
  <div class="tagline">Your online <b>learning center</b></div>
  <div class="header-rule"></div>
</header>
<nav class="main-nav">
  <a href="#" style="left:145px">HOME</a>
  <a href="#" style="left:340px">ABOUT US</a>
  <a href="#" class="active">OUR PRODUCTS</a>
  <a href="#" style="left:805px">SUBSCRIBE</a>
  <a href="#" style="left:1027px">CONTACT US</a>
</nav>

<article class="card card--problem">
  <div class="card-head">GOT A PROBLEM?</div>
  <div class="card-media" role="img" aria-label="Screenshot of the Scribo 2007 editor with an empty page" style="background:linear-gradient(180deg,#dbe7f5 0%,#c5d8ee 28%,#fff 30%,#fff 92%,#cfdcec 100%)"></div>
  <div class="pager"><span class="current">1</span><span>2</span><span>3</span><span>4</span><span>5</span><span>6</span><span>7</span></div>
  <h2 class="card-title">Problem with Scribo 2007 paragraph spacing</h2>
  <p class="card-text">Why is there extra space after each paragraph in Scribo 2007? How to I work around it? How do you change it back to how it was in Scribo 2003?</p>
  <a class="more" href="#">More</a>
</article>

<article class="card card--expert">
  <div class="card-head">BE AN EXPERT!</div>
  <div class="card-media" role="img" aria-label="Screenshot of an e-mail message window with voting options" style="background:linear-gradient(180deg,#e3ebf5 0%,#d6e2f0 28%,#f7f9fc 30%,#fff 100%)"></div>
  <div class="pager"><span class="current">1</span><span>2</span><span>3</span><span>4</span><span>5</span><span>6</span><span>7</span></div>
  <h2 class="card-title">Add voting buttons to an e-mail</h2>
  <p class="card-text">Voting buttons allow you to give recipients of your email a choice they can select with just a click over a button.</p>
  <a class="more" href="#">More</a>
</article>

<div class="search">Search</div>
<div class="search-btn">GO</div>
<div class="advanced">Advanced options</div>

<aside class="login">
  <h2>MEMBER LOG IN</h2>
  <div class="field"><label>User name</label><span></span></div>
  <div class="field"><label>Password</label><span></span></div>
  <span class="forgot">Forgoten your password</span>
</aside>

<aside class="info">
  <section>
    <h3>Set up an account</h3>
    <p>Want to know more about how you can store your notes on Vormalink.</p>
    <a class="more" href="#">More</a>
  </section>
  <section>
    <h3>Subscribe</h3>
    <p>Want to subscribe to Vormalink</p>
    <a class="more" href="#">More</a>
  </section>
</aside>

<div class="footer-band"></div>
<footer class="copyright">Copyright © 2009 Vormalink. Use of this Web site constitutes acceptance of the <a href="#">User Agreement</a>.</footer>
</body>
</html>
```